Redesign PixelHarbor's Designer Account Home Page

Are a web designer? New to PixelHarbor? This contest is for you!

We want you to redesign PixelHarbor's designer account home page. We're looking for bold and innovative ideas to make this page a useful and fun experience for you and your fellow designers.

Only new registrants this month are eligible to enter this contest and win prizes.

Your task:
* We want you to put your web design skills to the test and re-design the My Account home page ("Overview") on PixelHarbor to make it more functional and engaging for designers on PixelHarbor.
* The page you are redesigning is here: http://www.pixelharbor-example.com/my-profile.
* Your design should allow for the same functionality as the existing page, though you don't need to replicate the same elements (buttons) or the same menu structure.
* Your design must fit with the branding of the site.
* You must provide a brief outline of what changes you made and why when you upload your design
* 1 submission per designer - make it your best work!
* Pls see "Must haves" for requirements.

Deadline:
* Submit before 12:00am 1st September UTC. Pls convert this deadline to your local timezone and take note of the local time and date

Prizes: $1,000 to win
* First prize for the best design is $700
* Second prize is $200
* Third prize is $100

If you started from scratch, how would you design the MyAccount page on PixelHarbor?

Good luck & have fun!

Mel / The PixelHarbor Team

Target Market(s)

PixelHarbor designers

Number of Pages Required

1 page

Requirements
Must have
• Dimensions: 1200 x 1000 px
• Minimum 150-300 dpi
• Your design must adhere to our quality standards to be eligible to receive a prize
• Submissions must be created in Adobe Creative Suite (Illustrator or Photoshop)
• Your design must fit with the branding of the PixelHarbor site.
• Only new registrants this month are eligible to enter and win prizes.

```html
<!DOCTYPE html>
<html lang="en">
<head>
<meta charset="utf-8">
<title>PixelHarbor – My Account Overview</title>
<link rel="stylesheet" href="https://fonts.googleapis.com/css2?family=Open+Sans:wght@400;600;700;800&display=swap">
<style>
  :root{
    --green:#8cc63f;
    --green-dark:#76ad2c;
    --green-pale:#eef6e2;
    --ink:#3a3a3a;
    --muted:#8a8a8a;
    --faint:#b5b5b5;
    --line:#e2e2e2;
    --page:#f3f3f3;
    --panel:#ffffff;
    --header:#2b2b2b;
    --footer:#333333;
    --footer-deep:#292929;
  }
  *{box-sizing:border-box;margin:0;padding:0}
  html,body{width:889px;height:1200px;overflow:hidden}
  body{background:var(--page);font-family:"Open Sans",Arial,sans-serif;color:var(--ink);font-size:7px;line-height:1.35;position:relative}
  .wrap{width:550px;margin:0 auto;position:relative}

  /* top bar */
  .topbar{height:28px;background:var(--header)}
  .topbar .wrap{display:flex;align-items:center;height:28px;gap:14px}
  .brand{display:flex;align-items:center;gap:4px;color:#fff;font-weight:700;font-size:10px}
  .brand i{width:8px;height:8px;background:var(--green);display:block}
  .nav{display:flex;gap:9px;color:#c9c9c9;font-size:6px}
  .search{margin-left:auto;display:flex;gap:3px}
  .search span{height:11px;width:48px;background:#fff;border-radius:2px;font-size:5.5px;color:var(--muted);padding:1px 4px}
  .search b{height:11px;width:34px;background:var(--green);border-radius:2px;font-size:5.5px;color:#fff;text-align:center;line-height:11px}

  .crumbs{height:26px;background:#e9e9e9;border-bottom:1px solid var(--line)}
  .crumbs .wrap{display:flex;align-items:flex-end;height:26px;gap:3px}
  .crumbs span{background:#dcdcdc;padding:3px 10px;font-size:6px;color:var(--muted);border-radius:2px 2px 0 0}
  .crumbs span.on{background:#fff;color:var(--ink)}

  h1.page-title{font-size:14px;font-weight:700;letter-spacing:.5px;padding:36px 0 10px}

  .panel{background:var(--panel);border:1px solid var(--line);border-radius:2px}

  /* profile card */
  .profile{height:172px;display:flex;flex-direction:column}
  .profile-top{display:flex;gap:14px;padding:14px 16px 10px;flex:1}
  .avatar{width:58px;height:58px;border-radius:50%;background:linear-gradient(#dfe7ef,#9fb3c6);flex:none}
  .profile-text{flex:1}
  .profile-text h2{font-size:11px;color:var(--green);font-weight:800;margin-bottom:4px}
  .profile-text p{color:var(--muted);font-size:5.6px;line-height:1.5}
  .btn{background:var(--green);color:#fff;font-weight:700;font-size:6px;border-radius:2px;text-align:center;display:inline-block}
  .profile .btn{height:15px;line-height:15px;width:70px;align-self:flex-start}
  .stats{display:flex;border-top:1px solid var(--line);height:72px}
  .stat{flex:1;text-align:center;padding-top:8px;border-right:1px solid var(--line);border-bottom:3px solid var(--line)}
  .stat:last-child{border-right:none}
  .stat.hit{border-bottom-color:var(--green)}
  .stat small{display:block;color:var(--muted);font-size:5.5px}
  .stat strong{display:block;color:var(--green);font-size:15px;font-weight:700;line-height:1.3}
  .stat em{font-style:normal;color:var(--faint);font-size:5px}

  /* body */
  .layout{display:flex;gap:10px;margin-top:14px}
  .sidebar{width:80px;flex:none;align-self:flex-start}
  .sidebar a{display:block;height:19px;line-height:19px;padding-left:9px;font-size:6px;color:var(--muted);border-bottom:1px solid var(--line);text-decoration:none}
  .sidebar a.on{background:var(--green);color:#fff;font-weight:600}
  .content{flex:1;display:flex;flex-direction:column;gap:12px}

  .panel-head{display:flex;justify-content:space-between;align-items:center;padding:9px 12px 4px}
  .panel-head h3{font-size:7.5px;font-weight:600}
  .panel-head span{color:var(--green);font-weight:700;font-size:6px}
  .progress{margin:2px 12px 10px;height:10px;background:#e8e8e8;border-radius:2px;overflow:hidden}
  .progress i{display:block;width:48%;height:100%;background:var(--green)}
  .todo{padding:0 12px 10px}
  .todo h4{color:var(--green);font-size:7px;margin-bottom:4px}
  .todo li{list-style:none;height:17px;display:flex;align-items:center;justify-content:space-between;padding:0 6px;border:1px solid var(--line);margin-bottom:3px;font-size:5.6px;color:var(--muted)}
  .todo li.done{background:var(--green-pale);border-color:#cfe4b0;color:var(--green-dark)}
  .todo li i{width:10px;height:10px;border:1px solid #cfcfcf;background:#f6f6f6;border-radius:2px;display:block}
  .todo li.done i{background:var(--green);border-color:var(--green)}
  .panel-sub{padding:0 12px 6px;color:var(--faint);font-size:5.5px}

  .jobs{padding:0 12px 10px}
  .job{display:flex;align-items:center;height:30px;border-top:1px solid var(--line)}
  .job-info{flex:1}
  .job-info b{display:block;color:var(--green);font-size:6.4px}
  .job-info span{color:var(--faint);font-size:5.2px}
  .job-num{width:30px;text-align:center;font-size:6px;font-weight:700}
  .job-num small{display:block;font-weight:400;color:var(--faint);font-size:4.6px}
  .job .btn{width:44px;height:13px;line-height:13px;margin-left:8px}

  .notes{padding:0 12px 12px}
  .note{display:flex;align-items:center;gap:8px;height:34px;border-top:1px solid var(--line)}
  .note i{width:18px;height:18px;border-radius:50%;background:#d8d8d8;display:flex;align-items:center;justify-content:center;flex:none}
  .note b{display:block;font-size:6.2px}
  .note span{color:var(--faint);font-size:5.2px}

  /* footer */
  .footer{position:absolute;left:0;top:1000px;width:889px;height:200px;background:var(--footer);color:#bdbdbd}
  .footer .wrap{display:flex;gap:22px;padding-top:18px}
  .fcol h5{color:#fff;font-size:6.8px;margin-bottom:6px}
  .fcol li{list-style:none;font-size:5.3px;line-height:1.9}
  .tags{display:flex;flex-wrap:wrap;gap:3px;width:92px}
  .tags span{border:1px solid #555;padding:1px 3px;font-size:5px}
  .subscribe span{display:block;height:11px;width:100px;background:#fff;border-radius:2px;margin-bottom:8px}
  .dots{display:flex;gap:4px;margin-bottom:7px}
  .dots i{width:11px;height:11px;border-radius:50%;background:#666;display:block}
  .dots.sq i{border-radius:1px;width:13px;height:9px;background:#777}
  .footer-base{position:absolute;left:0;bottom:0;width:100%;height:22px;background:var(--footer-deep)}
  .footer-base .wrap{padding-top:7px;font-size:5px;color:#888}
</style>
</head>
<body>
  <header class="topbar">
    <div class="wrap">
      <div class="brand"><i></i>PixelHarbor</div>
      <nav class="nav"><span>Categories</span><span>Designers</span><span>Browse Jobs</span><span>How it works</span></nav>
      <div class="search"><span>My Account</span><b>Search</b></div>
    </div>
  </header>
  <div class="crumbs"><div class="wrap"><span>Home</span><span class="on">My Profile</span></div></div>

  <main class="wrap">
    <h1 class="page-title">OVERVIEW</h1>

    <section class="panel profile">
      <div class="profile-top">
        <div class="avatar" role="img" aria-label="Designer profile photo placeholder"></div>
        <div class="profile-text">
          <h2>MARLOWE</h2>
          <p>Freelance designer focused on clean brand identities, friendly web layouts and bold print pieces. I enjoy turning rough ideas into clear visuals and working closely with clients through every round of feedback until the result feels right for their audience and goals.</p>
        </div>
        <span class="btn">UPLOAD PHOTO</span>
      </div>
      <div class="stats">
        <div class="stat hit"><small>Rank</small><strong>#1001</strong><em>Top designers this month</em></div>
        <div class="stat"><small>Profile</small><strong>100%</strong><em>Fully complete</em></div>
        <div class="stat hit"><small>Submissions</small><strong>00</strong><em>Entries made so far</em></div>
        <div class="stat"><small>Earnings</small><strong>$0,000</strong><em>Total paid out</em></div>
      </div>
    </section>

    <div class="layout">
      <aside class="sidebar panel">
        <a class="on">Overview</a><a>Notifications</a><a>Inbox</a><a>Submissions</a><a>Messages</a><a>Wallet</a><a>Badges</a><a>Settings</a>
      </aside>

      <div class="content">
        <section class="panel">
          <div class="panel-head"><h3>Getting Started - Complete your profile</h3><span>90% Complete</span></div>
          <div class="progress"><i></i></div>
          <ul class="todo">
            <h4>Things to do</h4>
            <li>Upload a profile photo<i></i></li>
            <li>Write a short bio<i></i></li>
            <li class="done">Add your skills<i></i></li>
            <li>Upload portfolio samples<i></i></li>
            <li>Verify your email address<i></i></li>
            <li class="done">Set payment details<i></i></li>
            <li>Enter your first contest<i></i></li>
          </ul>
        </section>

        <section class="panel">
          <div class="panel-head"><h3>Recommended Jobs</h3></div>
          <p class="panel-sub">Jobs picked for you based on your skills and recent activity</p>
          <div class="jobs">
            <div class="job"><div class="job-info"><b>New Logo for Cloud Based service</b><span>Logo design for a growing software startup</span></div><div class="job-num">36<small>Entries</small></div><div class="job-num">25<small>Days</small></div><div class="job-num">$300<small>Prize</small></div><span class="btn">VIEW JOB</span></div>
            <div class="job"><div class="job-info"><b>New Logo for Cloud Based service</b><span>Logo design for a growing software startup</span></div><div class="job-num">36<small>Entries</small></div><div class="job-num">25<small>Days</small></div><div class="job-num">$300<small>Prize</small></div><span class="btn">VIEW JOB</span></div>
            <div class="job"><div class="job-info"><b>New Logo for Cloud Based service</b><span>Logo design for a growing software startup</span></div><div class="job-num">36<small>Entries</small></div><div class="job-num">25<small>Days</small></div><div class="job-num">$300<small>Prize</small></div><span class="btn">VIEW JOB</span></div>
            <div class="job"><div class="job-info"><b>New Logo for Cloud Based service</b><span>Logo design for a growing software startup</span></div><div class="job-num">36<small>Entries</small></div><div class="job-num">25<small>Days</small></div><div class="job-num">$300<small>Prize</small></div><span class="btn">VIEW JOB</span></div>
            <div class="job"><div class="job-info"><b>New Logo for Cloud Based service</b><span>Logo design for a growing software startup</span></div><div class="job-num">36<small>Entries</small></div><div class="job-num">25<small>Days</small></div><div class="job-num">$300<small>Prize</small></div><span class="btn">VIEW JOB</span></div>
          </div>
        </section>

        <section class="panel">
          <div class="panel-head"><h3>Notifications</h3></div>
          <p class="panel-sub">Your latest updates from contests and clients</p>
          <div class="notes">
            <div class="note"><i><svg width="9" height="9" viewBox="0 0 10 10"><path d="M2 5l2 2 4-4" stroke="#fff" stroke-width="1.6" fill="none"/></svg></i><div><b>Welcome to PixelHarbor</b><span>Your account is ready to go</span></div></div>
            <div class="note"><i><svg width="9" height="9" viewBox="0 0 10 10"><rect x="1.5" y="2.5" width="7" height="5" stroke="#fff" fill="none"/></svg></i><div><b>You have a new message</b><span>A client replied to your entry</span></div></div>
            <div class="note"><i><svg width="9" height="9" viewBox="0 0 10 10"><path d="M5 1.5v7M1.5 5h7" stroke="#fff" stroke-width="1.4"/></svg></i><div><b>You've got a new badge</b><span>Keep entering to earn more</span></div></div>
          </div>
        </section>
      </div>
    </div>
  </main>

  <footer class="footer">
    <div class="wrap">
      <div class="fcol"><h5>I need a...</h5><ul><li>Logo design</li><li>Website design</li><li>Business card</li><li>Brochure design</li><li>T-shirt design</li></ul></div>
      <div class="fcol"><h5>Find a...</h5><ul><li>Logo designer</li><li>Web designer</li><li>Graphic designer</li><li>Print designer</li><li>Illustrator</li></ul></div>
      <div class="fcol"><h5>About us</h5><ul><li>How it works</li><li>Our story</li><li>Press</li><li>Careers</li><li>Contact</li></ul></div>
      <div class="fcol"><h5>Popular pages</h5><div class="tags"><span>Logos</span><span>Web</span><span>Print</span><span>Apps</span><span>Icons</span><span>Flyers</span><span>Labels</span></div></div>
      <div class="fcol subscribe"><h5>Subscribe to newsletter</h5><span></span><div class="dots"><i></i><i></i><i></i><i></i></div><div class="dots sq"><i></i><i></i><i></i><i></i></div><div class="dots sq"><i></i><i></i><i></i></div></div>
    </div>
    <div class="footer-base"><div class="wrap">© PixelHarbor. All rights reserved.</div></div>
  </footer>
</body>
</html>
```